依頼詳細
80-90年代の社会問題や表象をテーマにした市民参加型の調査サークルの部員募集のためのチラシです。
遊び心をもち、裏路地に入っていくことを想起するように、80年代後半~90年代初頭のピンクチラシをモチーフにデザインをお願いします。
記載項目
団体名:かわせみタンボウクラブ部(かわタン)
連絡先:Chatora:https//chatora-link.example/7kQmW2pX

必ず記載してほしい内容は下記です。
・仙台の社会活動を一緒に調査してくれるステキなアナタ!
・ただ今、部員募集!
・自由出勤(委細面接)
・経験者・未経験者
※なんでも、お気軽にご連絡下さい。
サイズ
A5
ページ数
片面
希望イメージ
シンプル 複雑
単色 カラフル
暗い 明るい
日常 高級
遊び心 厳粛
未来的 伝統的
女性的 男性的
希望する色
納品ファイル
• イラストレーター形式 (.ai)
• PNG形式 (.png)
補足説明
■ 選んだ理由

ご提案の内容を汲み取っていただき、活動の参加対象となる方にとって親しみあるデザインでしたので、採用させていただきました。

■ 提案者全員のお礼・コメント

ご提案大変ありがとうございました。難しいテーマにも関わらず、意図を汲み取っていただき、ユニークなご提案を多くいただきました。ご参加いたた皆様、大変ありがとうございました。

```html
<!DOCTYPE html>
<html lang="ja">
<head>
<meta charset="utf-8">
<title>かわせみタンボウクラブ部 部員募集</title>
<link rel="stylesheet" href="https://fonts.googleapis.com/css2?family=Shippori+Mincho+B1:wght@800&family=Dela+Gothic+One&family=Noto+Sans+JP:wght@500;700&display=swap">
<style>
  :root {
    --magenta: #ec1a7c;
    --hot-pink: #f0389a;
    --ink: #111111;
    --paper: #ffffff;
    --neon-yellow: #f5e64a;
    --night-blue: #1d1a4a;
    --neon-purple: #7a2bb8;
    --neon-cyan: #27b9d8;
  }
  * { box-sizing: border-box; margin: 0; padding: 0; }
  html, body { width: 847px; height: 1200px; overflow: hidden; background: var(--paper); }
  .flyer { position: relative; width: 847px; height: 1200px; background: var(--paper); font-family: "Shippori Mincho B1", serif; color: var(--ink); }
  .frame { position: absolute; left: 0; top: 0; width: 847px; height: 1108px; border: 22px solid var(--magenta); background: var(--paper); overflow: hidden; }
  .scene-art { position: absolute; left: 0; top: 92px; width: 803px; height: 994px;
    background:
      radial-gradient(ellipse at 55% 40%, #f3a07a 0%, rgba(243,160,122,0) 28%),
      radial-gradient(ellipse at 25% 70%, var(--neon-cyan) 0%, rgba(39,185,216,0) 35%),
      radial-gradient(ellipse at 85% 60%, var(--hot-pink) 0%, rgba(240,56,154,0) 40%),
      linear-gradient(160deg, var(--neon-purple) 0%, var(--night-blue) 55%, #3a1a5e 100%); }
  .headline { position: absolute; top: 4px; left: 0; width: 100%; display: flex; justify-content: space-between; padding: 0 40px; font-size: 104px; line-height: 1; letter-spacing: 4px; z-index: 2; }
  .eye-art { position: absolute; left: 344px; top: 18px; width: 116px; height: 62px; border-radius: 50%; background: radial-gradient(circle at 50% 50%, #3a2a1a 0 18%, #8a6a4a 19% 34%, #f1e6dc 35% 100%); z-index: 2; }
  .intro { position: absolute; left: 18px; top: 118px; width: 300px; font-size: 29px; line-height: 1.42; z-index: 2; }
  .intro span { background: var(--paper); padding: 0 2px; box-decoration-break: clone; -webkit-box-decoration-break: clone; }
  .call { position: absolute; left: 18px; top: 615px; width: 780px; font-family: "Noto Sans JP", sans-serif; font-weight: 700; font-size: 40px; line-height: 1.3; color: var(--paper); -webkit-text-stroke: 7px var(--ink); paint-order: stroke fill; z-index: 2; }
  .condition { position: absolute; left: 12px; width: 172px; background: var(--paper); border: 4px solid var(--magenta); font-size: 22px; line-height: 1.3; padding: 8px 10px; z-index: 2; }
  .condition.experience { top: 808px; }
  .condition.attendance { top: 902px; }
  .condition strong { font-size: 27px; }
  .club-name { position: absolute; left: 310px; top: 790px; width: 482px; height: 306px; background: var(--magenta); z-index: 2; padding: 30px 30px; font-family: "Dela Gothic One", sans-serif; color: var(--neon-yellow); font-size: 66px; line-height: 1.12; }
  .club-name small { display: block; margin-top: 10px; font-size: 40px; }
  .footer { position: absolute; left: 0; top: 1124px; width: 847px; height: 76px; display: flex; align-items: center; gap: 14px; padding: 0 8px; font-family: "Noto Sans JP", sans-serif; }
  .footer .label { background: var(--ink); color: var(--paper); font-weight: 700; font-size: 17px; padding: 6px 10px; }
  .footer .address { font-weight: 500; font-size: 19px; flex: 1; }
  .footer .note { font-size: 17px; line-height: 1.35; width: 150px; }
</style>
</head>
<body>
<div class="flyer">
  <div class="frame">
    <div class="scene-art" role="img" aria-label="ネオン街を背景にした女性のカラフルなイラスト"></div>
    <h1 class="headline"><span>部員</span><span>募集</span></h1>
    <div class="eye-art" role="img" aria-label="見開いた目のイラスト"></div>
    <p class="intro"><span>仙台の80-90年代の社会問題や表象をテーマにした市民参加型の調査サークル</span></p>
    <p class="call">仙台の社会活動を一緒に調査してくれるステキなアナタ!<br>ぜひご応募ください!</p>
    <p class="condition experience">経験者・未経験者<br>問いません</p>
    <p class="condition attendance"><strong>自由出勤</strong><br>(委細面接)</p>
    <div class="club-name">かわせみタンボウクラブ部<small>通称：かわタン</small></div>
  </div>
  <div class="footer">
    <span class="label">連絡先</span>
    <span class="address">Chatora：https//chatora-link.example/7kQmW2pX</span>
    <span class="note">なんでも、お気軽にご連絡下さい。</span>
  </div>
</div>
</body>
</html>
```